Business Card Design Project - bel soravin group

dear Sirs

we need business card design for our group ( BEL Soravin Group ) , i have got the Logo design of our group from pixel harbor in previous , so all need details relating to our group i think available with you, as well as the the chosen logo design

we hope to provide us with business card logo that to be appropaite and satisfactory to us .

thanks

note : logo design of our group is attached .
Updates

Reason: please extend the deadline of my project for additional 15 days because i didn't received appropriate design for our gruop yet . kindly beaware that i have received 77 design till now , supossed to send me 200-250 design at least . thanks

Target Market(s)

contents
-

name : Korvan EL Mistrani

position : Operation Manager

Industry/Entity Type

Business

Requirements
Must have

• person name

group logo
Nice to have
• logo color matching with back background

```html
<!DOCTYPE html>
<html lang="en">
<head>
<meta charset="utf-8">
<title>BEL Soravin Group – Business Card</title>
<link rel="stylesheet" href="https://fonts.googleapis.com/css2?family=Open+Sans:wght@400;600;700&display=swap">
<style>
  :root {
    --brand-blue: #0b4f92;
    --brand-blue-light: #2f7cc4;
    --ink-grey: #4a4a4a;
    --card-white: #ffffff;
    --backdrop: #e9e6e2;
  }
  * { box-sizing: border-box; margin: 0; padding: 0; }
  html, body { width: 1200px; height: 758px; overflow: hidden; }
  body {
    background: var(--backdrop);
    font-family: "Open Sans", Arial, sans-serif;
    position: relative;
  }
  .card {
    position: absolute;
    top: 229px;
    width: 520px;
    height: 300px;
    border-radius: 26px;
    overflow: hidden;
    box-shadow: 0 6px 18px rgba(0,0,0,0.18);
  }
  .card-front { left: 50px; background: var(--card-white); }
  .card-back { left: 630px; background: var(--brand-blue); }

  .front-wave { position: absolute; left: 0; top: 0; width: 520px; height: 300px; }

  .brand-mark {
    position: absolute;
    display: flex;
    align-items: center;
    gap: 12px;
    font-weight: 700;
    letter-spacing: 1px;
    white-space: nowrap;
  }
  .brand-square { display: block; flex: none; }
  .card-front .brand-mark { left: 38px; top: 44px; font-size: 30px; color: var(--brand-blue); }
  .card-front .brand-square { width: 22px; height: 22px; background: var(--brand-blue); }
  .card-back .brand-mark { left: 64px; top: 104px; font-size: 34px; color: var(--card-white); }
  .card-back .brand-square { width: 26px; height: 26px; background: var(--card-white); }

  .person {
    position: absolute;
    left: 40px;
    top: 136px;
    white-space: nowrap;
  }
  .person-name { font-size: 19px; font-weight: 700; color: var(--brand-blue); }
  .person-role { font-size: 12px; color: var(--ink-grey); }

  .contact-list {
    position: absolute;
    left: 40px;
    top: 168px;
    list-style: none;
    font-size: 12.5px;
    color: var(--ink-grey);
    line-height: 17px;
  }
  .contact-list li { display: flex; align-items: center; gap: 6px; }
  .contact-list svg { width: 9px; height: 9px; fill: var(--ink-grey); flex: none; }

  .address {
    position: absolute;
    right: 34px;
    top: 182px;
    text-align: right;
    font-size: 12px;
    line-height: 16px;
    color: var(--card-white);
  }

  .website {
    position: absolute;
    left: 0;
    width: 100%;
    top: 196px;
    text-align: center;
    font-size: 19px;
    letter-spacing: 1.5px;
    color: var(--card-white);
  }
</style>
</head>
<body>

<section class="card card-front" aria-label="Business card front">
  <svg class="front-wave" viewBox="0 0 520 300" aria-hidden="true">
    <path d="M0 300 L0 280 C200 302 300 256 390 190 C450 150 490 138 520 136 L520 300 Z" fill="var(--brand-blue)"/>
    <path d="M0 272 C200 294 300 248 390 181 C450 141 490 129 520 127" fill="none" stroke="var(--brand-blue-light)" stroke-width="3"/>
  </svg>

  <div class="brand-mark"><span class="brand-square"></span>BEL SORAVIN GROUP</div>

  <div class="person">
    <span class="person-name">Korvan EL Mistrani,</span>
    <span class="person-role">Operation Manager</span>
  </div>

  <ul class="contact-list">
    <li><svg viewBox="0 0 10 10"><rect x="2.5" y="0" width="5" height="10" rx="1"/></svg>+2347031946628</li>
    <li><svg viewBox="0 0 10 10"><path d="M2 0 L4 2.5 L3 4 Q4.5 6 6 7 L7.5 6 L10 8 L8.5 10 Q3 9 0 1.5 Z"/></svg>+2347031946628</li>
    <li><svg viewBox="0 0 10 10"><circle cx="5" cy="3" r="2.6"/><path d="M0 10 Q5 3.5 10 10 Z"/></svg>+2347031946628</li>
    <li><svg viewBox="0 0 10 10"><rect x="0" y="1.5" width="10" height="7"/></svg>name@tarvellohotels.com</li>
    <li><svg viewBox="0 0 10 10"><circle cx="5" cy="5" r="4.8"/></svg>www.website.com</li>
  </ul>

  <p class="address">Street name, City<br>State, zip code</p>
</section>

<section class="card card-back" aria-label="Business card back">
  <div class="brand-mark"><span class="brand-square"></span>BEL SORAVIN GROUP</div>
  <p class="website">www.website.com</p>
</section>

</body>
</html>
```